Website Design for Law Firm

We need a fresh new website design for our client 'Torvek Legal' who specialises as a Criminal, Traffic & Civil Lawyer in Perth, Western Australia. We are looking for a very clean, professional and elegant look for the website, a presence of power and class needed as he deals with high end clients. Black, Silver and hints of gold need to run through the design without making the site look too dark. We are after a very modern, spacious web look, use of large readable text with links to social media (such as Facebook, Google+, Twitter, LinkedIn) to stand out and his contact details to be made very predominate.

Reason: Public holidays here in Australia, need more business hours to discuss designs with client.

Reason: Client needs more time to look through designs.

Reason: Client is going over last of designs. Design will be picked early next week!

Law Firm

```html
<!DOCTYPE html>
<html lang="en">
<head>
<meta charset="utf-8">
<title>Torvek Legal — Qualified Lawyer Perth WA</title>
<link href="https://fonts.googleapis.com/css2?family=Roboto+Condensed:wght@400;700&family=Open+Sans:wght@400;600;700&display=swap" rel="stylesheet">
<style>
  :root {
    --ink: #222222;
    --text: #444444;
    --muted: #666666;
    --rule: #d9d9d9;
    --dark: #262324;
    --darker: #1b1a1a;
    --white: #ffffff;
    --card: #dcdcdc;
    --wood-dark: #3a1c0e;
    --wood-mid: #7a3d1c;
    --wood-light: #c07a52;
    --footer-text: #e6e6e6;
    --footer-rule: #4a4646;
  }
  * { box-sizing: border-box; margin: 0; padding: 0; }
  html, body { width: 1057px; height: 1200px; overflow: hidden; }
  body {
    position: relative;
    background: var(--white);
    font-family: "Open Sans", Verdana, sans-serif;
    color: var(--text);
  }
  .hero {
    position: absolute; left: 0; top: 0; width: 1057px; height: 335px;
    background:
      radial-gradient(ellipse 420px 200px at 300px 150px, rgba(150,75,35,0.9), transparent 70%),
      radial-gradient(ellipse 500px 260px at 900px 60px, rgba(215,150,140,0.8), transparent 70%),
      linear-gradient(180deg, var(--wood-mid) 0%, var(--wood-dark) 60%, var(--wood-mid) 100%);
  }
  .logo-box {
    position: absolute; left: 142px; top: 0; width: 184px; height: 101px;
    background: var(--white); border-radius: 0 0 4px 4px;
    display: flex; align-items: center; justify-content: center; gap: 8px;
  }
  .logo-box .mark { width: 14px; height: 14px; background: var(--dark); }
  .logo-box .name {
    font-family: "Roboto Condensed", sans-serif; font-weight: 700;
    font-size: 27px; color: var(--dark); letter-spacing: 1px; line-height: 1;
  }
  .topbar {
    position: absolute; left: 600px; top: 0; width: 316px; height: 27px;
    background: var(--darker); border-radius: 0 0 4px 4px;
    font-size: 10px; color: #cccccc;
    display: flex; align-items: center; justify-content: space-around;
  }
  .topbar b { color: var(--white); font-size: 12px; }
  .topbar u { color: var(--white); }
  .hero-title {
    position: absolute; right: 142px; top: 124px; text-align: right;
    font-family: "Roboto Condensed", sans-serif; font-weight: 700;
    color: var(--white); line-height: 1.15; text-shadow: 0 1px 3px rgba(0,0,0,0.5);
  }
  .hero-title .l1 { font-size: 29px; }
  .hero-title .l2 { font-size: 23px; }
  .nav {
    position: absolute; left: 0; top: 335px; width: 1057px; height: 36px;
    background: linear-gradient(#ffffff, #ececec); border-bottom: 1px solid #d6d6d6;
  }
  .nav ul { position: absolute; left: 142px; display: flex; list-style: none; height: 36px; }
  .nav li {
    font-size: 11px; color: #222; padding: 0 16px; line-height: 36px;
    border-right: 1px solid #cfcfcf;
  }
  .nav li.active { background: var(--dark); color: var(--white); }
  .nav li:last-child { border-right: 1px solid #cfcfcf; }
  h2.section {
    font-family: "Roboto Condensed", sans-serif; font-weight: 400;
    color: var(--ink); font-size: 25px;
  }
  .welcome { position: absolute; left: 142px; top: 408px; width: 466px; font-size: 10.3px; line-height: 14px; }
  .welcome .sub { color: var(--muted); font-size: 10.5px; padding: 4px 0 6px; border-bottom: 1px solid var(--rule); margin-bottom: 12px; }
  .welcome p { margin-bottom: 12px; }
  .welcome strong { color: var(--ink); font-weight: 400; }
  .welcome .hours u { color: var(--ink); }
  .welcome .hours b { color: var(--ink); }
  .col-divider { position: absolute; left: 659px; top: 414px; width: 1px; height: 240px; background: var(--rule); box-shadow: -3px 0 6px rgba(0,0,0,0.08); }
  .news { position: absolute; left: 702px; top: 408px; width: 213px; }
  .news h2 { padding-bottom: 13px; border-bottom: 1px solid var(--rule); }
  .news-item { display: flex; gap: 19px; padding: 16px 0 16px; border-bottom: 1px solid var(--rule); }
  .news-date {
    flex: 0 0 41px; height: 41px; background: var(--dark); color: var(--white);
    font-size: 10px; text-align: center; line-height: 14px; padding-top: 7px;
  }
  .news-date b { font-size: 11px; display: block; }
  .news-item p { font-size: 10.3px; line-height: 12.5px; color: var(--text); }
  .read-more { display: block; margin-top: 12px; font-size: 9.5px; font-weight: 700; color: var(--ink); text-decoration: underline; letter-spacing: 0.5px; }
  .hr { position: absolute; left: 142px; top: 700px; width: 773px; height: 1px; background: var(--rule); }
  .expertise-title { position: absolute; left: 0; width: 1057px; top: 720px; text-align: center; }
  .arrow { position: absolute; top: 828px; }
  .cards { position: absolute; left: 177px; top: 778px; display: flex; gap: 15px; }
  .card { width: 225px; text-align: center; }
  .card .frame { width: 225px; height: 135px; background: var(--card); padding: 11px 12px; }
  .card .photo { width: 100%; height: 100%; }
  .card h3 { font-family: "Roboto Condensed", sans-serif; font-weight: 400; font-size: 16px; color: var(--ink); margin-top: 16px; }
  .footer { position: absolute; left: 0; top: 1000px; width: 1057px; height: 200px; background: var(--darker); color: var(--footer-text); font-size: 10px; }
  .flist { position: absolute; top: 24px; list-style: none; line-height: 18.3px; }
  .flist li::before { content: "•"; margin-right: 7px; }
  .fdiv { position: absolute; top: 22px; width: 1px; height: 118px; background: var(--footer-rule); }
  .fhead { font-family: "Roboto Condensed", sans-serif; font-size: 16px; color: var(--white); }
  .pay { position: absolute; left: 418px; top: 18px; }
  .pay .cards-row { display: flex; gap: 9px; margin: 10px 0 8px; }
  .pay .cards-row span { width: 43px; height: 27px; background: var(--white); border-radius: 2px; }
  .pay .cards-row span:first-child { background: #1f3a6b; }
  .pay .cards-row span:last-child { background: #111; border: 1px solid #888; }
  .follow { position: absolute; left: 633px; top: 18px; }
  .follow .icons { display: flex; gap: 5px; margin-top: 9px; }
  .follow .icons span { width: 20px; height: 20px; background: #cfcfcf; }
  .fcontact { position: absolute; left: 787px; top: 22px; line-height: 1.25; }
  .fcontact .label { font-size: 10px; color: #cccccc; }
  .fcontact .big { font-size: 14px; color: var(--white); margin-bottom: 14px; }
  .fcontact u { color: var(--white); font-size: 10.5px; }
  .copyright { position: absolute; left: 142px; top: 160px; width: 773px; border-top: 1px solid var(--footer-rule); text-align: center; font-size: 9.5px; color: #bbbbbb; padding-top: 8px; line-height: 13px; }
  .copyright b { color: var(--white); }
  .copyright .trading { color: var(--white); }
</style>
</head>
<body>
  <header class="hero" role="img" aria-label="Photograph of a wooden judge's gavel and law books on a desk">
    <div class="logo-box"><span class="mark"></span><span class="name">TORVEK LEGAL</span></div>
    <div class="topbar"><span>Phone : <b>0400 318 742</b></span><span>Email : <u>info@torveklegal.com.au</u></span></div>
    <div class="hero-title"><div class="l1">QUALIFIED LAWYER</div><div class="l2">PERTH WA</div></div>
  </header>

  <nav class="nav">
    <ul>
      <li class="active">HOME</li><li>ABOUT US</li><li>PRACTICE AREA</li><li>SCOPE OF ADVICE</li><li>LEGAL COSTS</li><li>NEWS</li><li>PRESS</li><li>FAQ</li><li>CONTACT</li>
    </ul>
  </nav>

  <section class="welcome">
    <h2 class="section">Welcome to Our Site !</h2>
    <div class="sub">Criminal Defence Lawyer, Traffic Defence Lawyer &amp; Civil Litigation Lawyer, Perth WA</div>
    <p>Torvek Legal is an established law firm practicing in <strong>Criminal Law</strong>, <strong>Traffic Law</strong> and <strong>Civil Law</strong>. We are conveniently located close to the <strong>Perth Magistrates Court</strong> and <strong>District Court</strong>.</p>
    <p>We understand that facing legal proceedings is very daunting and our clients are always saying <strong>"we don't know what to expect, we haven't been through anything like this before"</strong>.</p>
    <p>We provide easy-to-understand advice and expert assistance to help you navigate complex court procedures. Our legal fees are open and transparent so you know from day one how much your legal defence is going to cost. We service all metropolitan courts as well as providing a visiting service to Karratha and Port Hedland.</p>
    <p class="hours"><u>Our office hours are</u> <b>: 8:30 - 5:00 pm Monday to Friday</b><br>(but appointments can be made outside of these times.)</p>
  </section>

  <div class="col-divider"></div>

  <aside class="news">
    <h2 class="section">Latest News</h2>
    <div class="news-item">
      <div class="news-date"><b>20</b>JUNE</div>
      <p>Lorem ipsum dolor sit amet, consectetur adipisicing elit, sed do eiusmod tempor incididunt ut labore et dolore magna aliqua ...</p>
    </div>
    <div class="news-item">
      <div class="news-date"><b>25</b>JUNE</div>
      <p>Lorem ipsum dolor sit amet, consectetur adipisicing elit, sed do eiusmod tempor incididunt ut ...</p>
    </div>
    <span class="read-more">READ MORE</span>
  </aside>

  <div class="hr"></div>
  <h2 class="section expertise-title">Area of Expertise</h2>

  <svg class="arrow" style="left:141px" width="10" height="34" viewBox="0 0 10 34"><path d="M8 1 L2 17 L8 33" fill="none" stroke="#333" stroke-width="1.3"/></svg>
  <svg class="arrow" style="left:906px" width="10" height="34" viewBox="0 0 10 34"><path d="M2 1 L8 17 L2 33" fill="none" stroke="#333" stroke-width="1.3"/></svg>

  <div class="cards">
    <div class="card">
      <div class="frame"><div class="photo" role="img" aria-label="Photograph of handcuffed hands" style="background:linear-gradient(135deg,#d2501a,#e8a070 55%,#b8b8b8)"></div></div>
      <h3>CRIMINAL DEFENCE</h3>
    </div>
    <div class="card">
      <div class="frame"><div class="photo" role="img" aria-label="Photograph of old law books on a shelf" style="background:linear-gradient(180deg,#5a1a14,#2a120c 45%,#9a7a4a 70%,#2a1a10)"></div></div>
      <h3>TRAFFIC LAW</h3>
    </div>
    <div class="card">
      <div class="frame"><div class="photo" role="img" aria-label="Photograph of a hand signing a document" style="background:linear-gradient(110deg,#e8d8c8,#c89878 45%,#1a1210 80%)"></div></div>
      <h3>CIVIL LAW</h3>
    </div>
  </div>

  <footer class="footer">
    <ul class="flist" style="left:142px"><li>Home</li><li>About Us</li><li>Practice Areas</li><li>Scope of Advice</li><li>Legal Costs</li></ul>
    <div class="fdiv" style="left:252px"></div>
    <ul class="flist" style="left:276px"><li>Press</li><li>Recent Cases</li><li>FAQ</li><li>Links</li><li>Contact</li><li>Service Policy</li></ul>
    <div class="fdiv" style="left:385px"></div>
    <div class="pay">
      <div class="fhead">we accept</div>
      <div class="cards-row"><span></span><span></span><span></span></div>
      <div>Other major credit cards accepted.</div>
    </div>
    <div class="fdiv" style="left:603px"></div>
    <div class="follow">
      <div class="fhead">FOLLOW US ON</div>
      <div class="icons"><span></span><span></span><span></span><span></span></div>
    </div>
    <div class="fdiv" style="left:758px"></div>
    <div class="fcontact">
      <div class="label">Phone :</div><div class="big">(08) 9470 2215</div>
      <div class="label">Mobile :</div><div class="big">0400 318 742</div>
      <div class="label">Email :</div><u>info@torveklegal.com.au</u>
    </div>
    <div class="copyright">Copyright © <b>Torvek Legal</b> 2014-15.All Right reserved.<br><span class="trading">TORVEK HOLDINGS PTY LTD TRADING</span></div>
  </footer>
</body>
</html>
```